Toy Company Needs a Web Site For a New Toy

We need a web site for a new toy called "Zippa Loop Trike". The bike is a plastic, non motorized ride on toy for kids ages 1.5 - 5 years of age. The bike is being launched in three colors, red, blue and pink, though we may include a black option too.

For the web site we want something bold and colorful that communicates fun, therefore NO dull colors like black or grey. Nothing too cluttered. We want the site to attract the attention of kids but also give the parents a sense of confidence in our professionalism as a trustworthy toy company. The home page should focus on the bike, with different views of the bike and a small write-up on some of its key features. We would also like the home page to have a video of the bike in play. A obvious link to the shopping basket must be present as well. The site must include a shopping basket and ordering system.

Attached is a screenshot of a site that has the colourfulness and playfulness that we are looking for. Please have a look.

The bike images attached are renderings from the CAD software, actual high res photos will be used when the site is developed.

The product logo is attached and MUST be used on the site. It must be BOLD and can be incorporated into the actual website design.

The site pages are:
Home
Gallery
Buy
Contact

Competitors:
www.brambleplay.example
www.quorvaride.example
I do not like either of their sites.

We only have one product at this time, so the site is to be focused on that product, not a whole catalog of products. It is really a single product with the ability to purchase.
Updates

Project Deadline Extended
Reason: I am extending this competition in order to give me more time to review each design and provide the feedback that the designers deserve.

Target Market(s)

Parents, children ages 1.5 - 5.

Industry/Entity Type

It Company

Colors
0555a3
eb1f27
9bcb3c
faed22
f78f20
f37022
e34197
a6459a
6b449b

Requirements
Must have
• Please use the logo attached, but feel free to use different colors.
Should not have
• Dull colors like black and grey

```html
<!DOCTYPE html>
<html lang="en">
<head>
<meta charset="utf-8">
<title>Zippa Loop Trike</title>
<link href="https://fonts.googleapis.com/css2?family=Arimo:wght@400;700&family=Fredoka+One&family=PT+Serif&display=swap" rel="stylesheet">
<style>
:root{
  --sky:#bfe8f8;
  --blue:#1aa6dc;
  --blue-light:#2cb4e6;
  --navy:#0555a3;
  --green:#9bcb3c;
  --green-dark:#6fa321;
  --search:#6c9d23;
  --orange:#f78f20;
  --orange-dark:#f37022;
  --pink:#e34197;
  --purple:#a6459a;
  --white:#ffffff;
  --cloud:#f4fbfe;
  --cloud-line:#8fd6ef;
  --panel-line:#c9ecf8;
  --card-line:#bfe9ef;
  --text:#3b3b3b;
  --text-soft:#6a6a6a;
  --teal:#29a9b8;
  --price:#e0661a;
  --salmon:#f38a6e;
}
*{box-sizing:border-box;margin:0;padding:0}
html,body{width:803px;height:1200px;overflow:hidden}
body{font-family:"Arimo",Arial,sans-serif;color:var(--text);background:var(--sky)}
.canvas{position:relative;width:803px;height:1200px;overflow:hidden;
  background:linear-gradient(180deg,#a9e0f6 0%,#c6ecfa 35%,#b4e4f7 70%,#9fdbf4 100%)}
.abs{position:absolute}
.display{font-family:"Fredoka One",Arial,sans-serif;font-weight:400}

/* top utility bar */
.topbar{left:80px;top:0;width:608px;height:26px;background:var(--green);border-radius:0 0 6px 6px;
  display:flex;align-items:center;font-size:9px;color:var(--white)}
.topbar span{padding:0 12px;border-right:1px solid rgba(255,255,255,.5);height:100%;display:flex;align-items:center}
.topbar .gap{flex:1;border:none}
.topbar .last{border-right:none}
.flag{display:inline-block;width:13px;height:8px;margin-left:3px;border-radius:1px}

/* brand */
.brand{left:96px;top:38px;display:flex;align-items:center;gap:8px}
.brand .dot{width:24px;height:24px;border-radius:50%;background:var(--blue)}
.brand .name{font-family:"Fredoka One",Arial,sans-serif;font-size:16px;color:var(--blue);line-height:1.1;width:96px}

/* basket status */
.basket-pill{left:574px;top:44px;width:150px;height:30px;border-radius:15px;background:var(--white);
  display:flex;align-items:center;gap:8px;padding-left:12px;font-size:7.5px;color:var(--text);
  box-shadow:0 1px 3px rgba(0,80,120,.18)}
.basket-links{left:540px;top:92px;width:182px;text-align:right;font-size:8px;color:var(--navy)}

/* nav */
.nav{left:80px;top:116px;width:640px;height:36px;background:var(--green);border-radius:18px;
  border-bottom:3px solid var(--green-dark);display:flex;align-items:center;padding-left:14px}
.nav a{font-family:"Fredoka One",Arial,sans-serif;font-size:14px;color:var(--white);text-decoration:none;margin-right:38px;padding:3px 10px;border-radius:14px}
.nav a.active{background:var(--green-dark)}
.search{position:absolute;right:8px;top:6px;width:174px;height:22px;border-radius:11px;background:var(--search);
  font-size:8px;color:#e8f5d4;padding:6px 12px}
.search svg{position:absolute;right:8px;top:5px}

/* colour pills */
.promo{left:80px;width:154px;height:72px;border-radius:36px;border:3px solid var(--white);box-shadow:0 2px 4px rgba(0,80,120,.25)}
.promo .thumb{position:absolute;left:6px;top:6px;width:54px;height:54px;border-radius:50%}
.promo h3{position:absolute;left:72px;top:14px;font-family:"Fredoka One",Arial,sans-serif;font-weight:400;font-size:9px;color:var(--white);letter-spacing:.3px}
.promo p{position:absolute;left:72px;top:30px;width:74px;font-size:6.5px;line-height:1.25;color:var(--white)}
.promo.blue{top:168px;background:var(--blue)} .promo.blue .thumb{background:#1283b8}
.promo.green{top:254px;background:var(--green)} .promo.green .thumb{background:#7aad2a}
.promo.orange{top:342px;background:var(--orange)} .promo.orange .thumb{background:#e07313}

/* hero */
.hero-frame{left:262px;top:170px;width:462px;height:244px;background:var(--cloud);
  border:6px solid var(--cloud-line);border-radius:48px}
.hero-bike{left:300px;top:210px;width:164px;height:150px;border-radius:20px;
  background:radial-gradient(ellipse at 50% 55%,#e9eef2 0%,#d6dde3 60%,#f2f5f7 100%)}
.hero-title{left:476px;top:250px;font-family:"PT Serif",serif;font-size:10.5px;font-weight:400;color:var(--teal)}
.hero-copy{left:476px;top:268px;width:206px;font-size:6.8px;line-height:1.35;color:var(--text-soft)}
.shop{left:618px;top:336px;width:66px;height:24px;border-radius:12px;background:#7dd3ea;border:2px solid var(--white);
  font-size:7.5px;color:var(--white);text-align:center;line-height:20px}
.hero-dots{left:642px;top:197px;display:flex;gap:5px}
.hero-dots i{width:6px;height:6px;border-radius:50%;background:#4a7d96}

/* main panel */
.main{left:80px;top:450px;width:466px;height:552px;background:var(--white);border-radius:6px;border:4px solid var(--panel-line)}
.section-title{position:absolute;left:0;width:100%;text-align:center;font-family:"Fredoka One",Arial,sans-serif;font-weight:400;font-size:20px;color:var(--blue)}
.section-sub{position:absolute;left:0;width:100%;text-align:center;font-size:7px;color:var(--text)}
.divider{position:absolute;left:96px;width:280px;height:1px;background:#e4e4e4}
.card{position:absolute;width:86px}
.card .photo{width:84px;height:118px;border-radius:8px;border:3px solid var(--card-line)}
.card .price{position:absolute;left:10px;top:104px;width:66px;height:26px;border-radius:13px;background:var(--white);
  border:2px solid var(--card-line);font-size:10px;color:var(--price);text-align:center;line-height:22px}
.card h4{margin-top:14px;text-align:center;font-size:8.5px;font-weight:400;color:var(--teal)}
.card p{text-align:center;font-size:6.5px;font-weight:700;line-height:1.15;color:var(--text);margin-top:2px}
.add{margin:8px auto 0;width:78px;height:18px;border-radius:9px;background:var(--blue);font-size:7px;color:var(--white);
  display:flex;align-items:center;justify-content:center;gap:5px}
.add.hot{background:var(--orange)}

/* side */
.colours{left:556px;top:454px;width:140px;height:196px;background:var(--blue);border-radius:10px 18px 8px 8px}
.colours h3{position:absolute;left:0;width:124px;text-align:center;top:8px;font-family:"Fredoka One",Arial,sans-serif;font-weight:400;font-size:15px;color:var(--white)}
.colour-link{position:absolute;left:10px;width:110px;height:22px;background:var(--blue-light);border-radius:2px;font-size:7.5px;color:var(--white);
  display:flex;align-items:center;padding-left:8px;gap:8px}
.bubble{position:absolute;border-radius:50%;background:var(--blue)}
.cartbox{left:556px;top:652px;width:140px;height:136px;background:var(--white);border:2px solid var(--orange)}
.cartbox header{height:26px;background:var(--orange);font-family:"Fredoka One",Arial,sans-serif;font-size:15px;color:var(--white);display:flex;align-items:center;gap:8px;padding-left:8px}
.cartbox .row{display:flex;justify-content:space-between;font-size:7px;padding:0 8px}
.cartbox .row em{font-style:italic;color:var(--price)}
.btn-sm{position:absolute;left:12px;height:16px;font-size:7.5px;color:var(--white);display:flex;align-items:center;justify-content:center}
.video{left:556px;top:798px;width:140px;height:122px;background:linear-gradient(135deg,#5a4233,#8a6a52 50%,#3b2c25)}
.play{position:absolute;left:51px;top:42px;width:38px;height:38px;border-radius:50%;background:var(--orange-dark)}
.shipping{left:556px;top:924px;width:140px;height:78px;background:var(--salmon);color:var(--white);padding:10px 12px}
.shipping b{display:block;font-size:21px;line-height:.98;font-weight:400;letter-spacing:.5px}
.shipping small{display:block;margin-top:3px;font-size:7px}

/* footer */
.footer{left:80px;top:1020px;width:614px;height:144px;background:var(--white);border-radius:6px}
.footer h5{position:absolute;font-family:"Fredoka One",Arial,sans-serif;font-size:11px;font-weight:400}
.footer ul{position:absolute;list-style:none;font-size:6.8px;line-height:13px;color:var(--text)}
.store-photo{position:absolute;left:12px;top:36px;width:140px;height:40px;background:linear-gradient(180deg,#9cc4e0,#6f8fa8 60%,#8aa07a)}
.about{position:absolute;left:12px;top:84px;width:144px;font-size:6.8px;line-height:1.35}
.social{position:absolute;left:462px;top:38px;display:flex;gap:5px}
.social i{width:17px;height:17px;border-radius:50%}
.email{position:absolute;left:462px;top:92px;width:96px;height:14px;background:var(--navy);font-size:5.5px;color:#cfe3f5;padding:4px 5px}
.submit{position:absolute;left:462px;top:112px;width:48px;height:14px;background:#c5d9ee;border:1px solid #8aa8c8;font-size:6px;text-align:center;line-height:12px;color:var(--navy)}
.mail{position:absolute;left:564px;top:106px;width:24px;height:24px;border-radius:50%;background:#d5e6f4;border:2px solid var(--white);box-shadow:0 0 0 1px #9bbbd6}
.copyright{left:86px;top:1172px;font-size:6.5px;color:var(--text-soft)}
.pay{left:616px;top:1168px;width:74px;height:26px;background:#f3f5f8;border:1px solid #c8d0da;border-radius:2px}
.pay i{position:absolute;top:14px;width:14px;height:8px;border-radius:1px}
</style>
</head>
<body>
<div class="canvas">

  <svg class="abs" style="left:0;top:0" width="803" height="1200" aria-hidden="true">
    <g fill="#d8f2fc" opacity=".7">
      <ellipse cx="40" cy="480" rx="90" ry="40"/>
      <ellipse cx="760" cy="520" rx="80" ry="36"/>
      <ellipse cx="120" cy="1110" rx="140" ry="50"/>
      <ellipse cx="740" cy="1100" rx="120" ry="46"/>
      <ellipse cx="760" cy="260" rx="70" ry="30"/>
      <ellipse cx="30" cy="760" rx="70" ry="32"/>
    </g>
    <path d="M740 0 C760 30 790 40 803 42 L803 0 Z" fill="var(--pink)" opacity=".8"/>
    <path d="M760 0 C772 18 790 26 803 26 L803 0 Z" fill="var(--purple)" opacity=".7"/>
  </svg>

  <div class="abs topbar">
    <span>Login</span><span>My Account</span><span>Shopping Cart</span><span>Check Out</span>
    <span class="gap"></span>
    <span>Currency</span><span>$ £ €</span><span>Language</span>
    <span class="last"><i class="flag" style="background:#c8d4ea"></i><i class="flag" style="background:#e2b14c"></i></span>
  </div>

  <div class="abs brand">
    <span class="dot"></span>
    <span class="name">Zippa Loop Trike</span>
  </div>

  <div class="abs basket-pill">
    <svg width="16" height="13" viewBox="0 0 16 13" aria-hidden="true"><path d="M1 1 h3 l2 8 h8 l1-6 H5" fill="none" stroke="var(--green-dark)" stroke-width="1.6"/><circle cx="7" cy="11.5" r="1.3" fill="var(--green-dark)"/><circle cx="13" cy="11.5" r="1.3" fill="var(--green-dark)"/></svg>
    Now in your cart 0 item
  </div>
  <div class="abs basket-links">My Basket &nbsp;•&nbsp; View Basket (Your Basket is Empty)</div>

  <nav class="abs nav">
    <a>Home</a><a class="active">Gallery</a><a>Buy</a><a>Contact</a>
    <div class="search">Search...
      <svg width="12" height="12" viewBox="0 0 12 12" aria-hidden="true"><circle cx="5" cy="5" r="3.5" fill="none" stroke="#fff" stroke-width="1.6"/><line x1="7.5" y1="7.5" x2="11" y2="11" stroke="#fff" stroke-width="1.8"/></svg>
    </div>
  </nav>

  <div class="abs promo blue"><div class="thumb" role="img" aria-label="Blue Zippa Loop Trike"></div><h3>LOREM IPSUM</h3><p>Simply dummy text of the printing and...</p></div>
  <div class="abs promo green"><div class="thumb" role="img" aria-label="Red Zippa Loop Trike"></div><h3>LOREM IPSUM</h3><p>Simply dummy text of the printing and...</p></div>
  <div class="abs promo orange"><div class="thumb" role="img" aria-label="Pink Zippa Loop Trike"></div><h3>LOREM IPSUM</h3><p>Simply dummy text of the printing and...</p></div>

  <div class="abs hero-frame"></div>
  <div class="abs hero-bike" role="img" aria-label="Zippa Loop Trike, side view"></div>
  <div class="abs hero-dots"><i></i><i></i><i></i><i></i></div>
  <h2 class="abs hero-title">THE STANDARD LOREM IPSUM PASSAGE</h2>
  <p class="abs hero-copy">Sed ut perspiciatis unde omnis iste natus error sit voluptatem accusantium doloremque laudantium, totam rem aperiam, eaque ipsa quae ab illo inventore veritatis et quasi architecto beatae vitae dicta sunt explicabo. Nemo enim ipsam voluptatem quia voluptas sit aspernatur aut odit aut fugit, sed quia consequuntur magni dolores eos qui ratione voluptatem sequi nesciunt.</p>
  <div class="abs shop">SHOP NOW!</div>

  <section class="abs main">
    <h2 class="section-title" style="top:14px">Featured Views</h2>
    <p class="section-sub" style="top:40px">Lorem ipsum dolor sit amet, consectetur adipisicing elit, sed do eiusmod tempor</p>

    <div class="card" style="left:8px;top:56px"><div class="photo" role="img" aria-label="Child riding the red trike" style="background:linear-gradient(160deg,#d7d2c8,#b78a7a 60%,#e9c54a)"></div><div class="price">$120.00</div><h4>Red Trike ...</h4><p>Lorem ipsum dolor sit amet consectetur adipisicing elit,</p><div class="add">🛒 Add to cart</div></div>
    <div class="card" style="left:128px;top:56px"><div class="photo" role="img" aria-label="Toddler on the blue trike" style="background:linear-gradient(160deg,#bfc3c2,#5b6670 60%,#e2a13a)"></div><div class="price">$135.00</div><h4>Blue Trike ...</h4><p>Lorem ipsum dolor sit amet consectetur adipisicing elit,</p><div class="add hot">🛒 Add to cart</div></div>
    <div class="card" style="left:248px;top:56px"><div class="photo" role="img" aria-label="Trike seen from the side" style="background:linear-gradient(160deg,#f6f6f6,#d9dcdf 60%,#c84040)"></div><div class="price">$180.00</div><h4>Side View ...</h4><p>Lorem ipsum dolor sit amet consectetur adipisicing elit,</p><div class="add">🛒 Add to cart</div></div>
    <div class="card" style="left:370px;top:56px"><div class="photo" role="img" aria-label="Child on the pink trike" style="background:linear-gradient(160deg,#f4f4f4,#d34080 55%,#e8e8e8)"></div><div class="price">$120.00</div><h4>Pink Trike ...</h4><p>Lorem ipsum dolor sit amet consectetur adipisicing elit,</p><div class="add">🛒 Add to cart</div></div>

    <div class="divider" style="top:290px"></div>

    <h2 class="section-title" style="top:310px">Coming Soon</h2>
    <p class="section-sub" style="top:336px">Lorem ipsum dolor sit amet, consectetur adipisicing elit, sed do eiusmod tempor</p>

    <div class="card" style="left:8px;top:362px"><div class="photo" role="img" aria-label="Two children riding trikes outdoors" style="background:linear-gradient(170deg,#c7dce8,#8aa38a 55%,#c9c9c2)"></div><div class="price">$120.00</div><h4>Black Trike ...</h4><p>Lorem ipsum dolor sit amet consectetur adipisicing elit,</p></div>
    <div class="card" style="left:128px;top:362px"><div class="photo" role="img" aria-label="Trike on grass" style="background:linear-gradient(170deg,#3e5a2a,#2f4ea0 55%,#5f7f3a)"></div><div class="price">$135.00</div><h4>Trike Bell ...</h4><p>Lorem ipsum dolor sit amet consectetur adipisicing elit,</p></div>
    <div class="card" style="left:248px;top:362px"><div class="photo" role="img" aria-label="Child riding the trike on a path" style="background:linear-gradient(170deg,#b9c2c4,#c8382f 50%,#a7a9a4)"></div><div class="price">$180.00</div><h4>Trike Basket ...</h4><p>Lorem ipsum dolor sit amet consectetur adipisicing elit,</p></div>
    <div class="card" style="left:370px;top:362px"><div class="photo" role="img" aria-label="Child riding the trike in a park" style="background:linear-gradient(170deg,#7fa86a,#3f82d0 50%,#d6cf3a)"></div><div class="price">$120.00</div><h4>Trike Helmet ...</h4><p>Lorem ipsum dolor sit amet consectetur adipisicing elit,</p></div>
  </section>

  <aside class="abs colours">
    <span class="bubble" style="left:130px;top:8px;width:14px;height:14px"></span>
    <span class="bubble" style="left:142px;top:24px;width:9px;height:9px"></span>
    <span class="bubble" style="left:134px;top:34px;width:7px;height:7px"></span>
    <h3>Trike Colours</h3>
    <div class="colour-link" style="top:34px">›››&nbsp; Red Trike</div>
    <div class="colour-link" style="top:60px">›››&nbsp; Blue Trike</div>
    <div class="colour-link" style="top:85px">›››&nbsp; Pink Trike</div>
    <div class="colour-link" style="top:111px">›››&nbsp; Black Trike</div>
    <div class="colour-link" style="top:136px">›››&nbsp; Spare Parts</div>
    <div class="colour-link" style="top:162px">›››&nbsp; Accessories</div>
  </aside>

  <aside class="abs cartbox">
    <header>
      <svg width="16" height="13" viewBox="0 0 16 13" aria-hidden="true"><path d="M1 1 h3 l2 8 h8 l1-6 H5" fill="none" stroke="#fff" stroke-width="1.6"/><circle cx="7" cy="11.5" r="1.3" fill="#fff"/><circle cx="13" cy="11.5" r="1.3" fill="#fff"/></svg>
      Cart
    </header>
    <p style="font-size:7px;padding:7px 8px;border-bottom:1px solid #e6e6e6">No Product</p>
    <div class="row" style="margin-top:7px"><span>Shipping</span><em>$0.00</em></div>
    <div class="row" style="margin-top:5px"><span>Total</span><em>$0.00</em></div>
    <div class="btn-sm" style="top:84px;width:36px;background:var(--orange-dark)">Cart</div>
    <div class="btn-sm" style="top:104px;width:58px;background:var(--green)">Check out</div>
  </aside>

  <div class="abs video" role="img" aria-label="Video of the Zippa Loop Trike in play">
    <div class="play"><svg width="38" height="38" viewBox="0 0 38 38" aria-hidden="true"><path d="M15 11 L27 19 L15 27 Z" fill="#fff"/></svg></div>
  </div>

  <div class="abs shipping"><b>FREE<br>SHIPPING</b><small>ON ORDERS OVER $900.</small></div>

  <footer class="abs footer">
    <h5 style="left:12px;top:14px;color:var(--blue)">About Store</h5>
    <div class="store-photo" role="img" aria-label="Store building"></div>
    <p class="about">Lorem ipsum dolor sit amet, consectetur adipisicing elit, sed do eiusmod tempor incididunt ut labore et dolore magna aliqua.</p>

    <h5 style="left:186px;top:14px;color:var(--orange)">What We Do!</h5>
    <ul style="left:188px;top:34px"><li>Lorem ipsum</li><li>Lorem ipsum</li><li>Lorem ipsum</li><li>Lorem ipsum</li><li>Lorem ipsum</li><li>Lorem ipsum</li></ul>

    <h5 style="left:308px;top:14px;color:var(--green-dark)">Consumer Services</h5>
    <ul style="left:310px;top:34px"><li>Check Order Status</li><li>Order Replacement Parts</li><li>Warranty Information</li><li>Recalls</li><li>FAQ's</li><li>Return Policy</li><li>Terms &amp; Conditions</li></ul>

    <h5 style="left:462px;top:14px;color:var(--navy)">Find us on</h5>
    <div class="social"><i style="background:#3b5f9c"></i><i style="background:#2ea6dd"></i><i style="background:#1a78b4"></i><i style="background:#f08a24"></i></div>
    <h5 style="left:462px;top:70px;color:var(--navy)">Sign Up For News letter</h5>
    <div class="email">enter your Email ID...</div>
    <div class="submit">SUBMIT</div>
    <div class="mail"><svg width="20" height="20" viewBox="0 0 20 20" aria-hidden="true"><rect x="4" y="6" width="12" height="8" fill="#fff" stroke="#5b86b0"/><path d="M4 6 L10 11 L16 6" fill="none" stroke="#5b86b0"/></svg></div>
  </footer>

  <p class="abs copyright">Copyright © 2013 Zippa Loop Trike. All Rights Reserved.</p>
  <div class="abs pay">
    <i style="left:4px;top:3px;width:40px;height:7px;background:#1f4f94"></i>
    <i style="left:4px;background:#d7a33a"></i><i style="left:21px;background:#2f5fa8"></i><i style="left:38px;background:#d9442e"></i><i style="left:55px;background:#8aa0b8"></i>
  </div>

</div>
</body>
</html>
```